Letterhead Design Project (logo provided)

We are a legal services provider company called DRV Legal based in the UK and would like some letterhead paper designed.

The design should use the attached logo, and should use the colors feature in the logo (along with blacks and/or greys).

The background paper must be white - and A4 size.

The letterhead should be provided in both .pdf and .doc (or .odf) formats.

Target Market(s)

Customers and clients for legal services

Industry/Entity Type

Legal

Requirements
Must have
• The header must include the following information:

Business name - DRV Legal LLP
Office address - Fennick Court, Wallingford, Oxfordshire OX10 4TJ, United Kingdom
Telephone - +44 (0)1632 960457
Email - post@ [domain given below]
Website: www.drvlegal-example.com

The footer must include the following information:

Registered office address - 14 Larkspur Row, Brindlecote, Wallingford, Oxfordshire OX10 4TW, United Kingdom
Companies House registration number - OC741593
VAT registration number - GB 417386025

```html
<!DOCTYPE html>
<html lang="en">
<head>
<meta charset="utf-8">
<title>DRV Legal LLP – Letterhead</title>
<link rel="stylesheet" href="https://fonts.googleapis.com/css2?family=Barlow:wght@400;500;600&display=swap">
<style>
  :root {
    --canvas: #ffffff;
    --paper: #ffffff;
    --rule: #222222;
    --ink: #111111;
    --brand-blue: #2f63ae;
    --brand-green: #3fae49;
    --tint-green: #c8e8c9;
    --tint-blue: #c2d1e8;
  }
  * { margin: 0; padding: 0; box-sizing: border-box; }
  html, body {
    width: 1200px;
    height: 1000px;
    overflow: hidden;
    background: var(--canvas);
    font-family: "Barlow", Arial, sans-serif;
    color: var(--ink);
  }
  .letterhead {
    position: absolute;
    left: 302px;
    top: 79px;
    width: 596px;
    height: 842px;
    background: var(--paper);
    border: 1px solid var(--rule);
    overflow: hidden;
  }
  .brand {
    position: absolute;
    left: 49px;
    top: 64px;
    display: flex;
    align-items: center;
    gap: 7px;
  }
  .brand-name {
    font-size: 27px;
    font-weight: 500;
    letter-spacing: 0.5px;
    color: var(--brand-blue);
    text-transform: uppercase;
    line-height: 1;
  }
  .brand-dot {
    width: 11px;
    height: 11px;
    border-radius: 50%;
    background: var(--brand-green);
  }
  .header-contact {
    position: absolute;
    left: 278px;
    top: 58px;
    font-size: 8.6px;
    line-height: 10.4px;
    font-weight: 500;
  }
  .header-contact .firm-name { font-weight: 600; }
  .footer-registration {
    position: absolute;
    left: 0;
    width: 512px;
    top: 779px;
    text-align: center;
    font-size: 7px;
    line-height: 10px;
    font-weight: 600;
  }
  .corner-decoration {
    position: absolute;
    left: 420px;
    top: 668px;
    width: 176px;
    height: 174px;
    border-top-left-radius: 88px;
    background: linear-gradient(135deg, var(--tint-green) 0%, var(--tint-green) 50%, var(--tint-blue) 100%);
  }
</style>
</head>
<body>
  <main class="letterhead">
    <div class="brand">
      <span class="brand-name">DRV Legal</span>
      <span class="brand-dot"></span>
    </div>

    <address class="header-contact" style="font-style: normal;">
      <div class="firm-name">DRV Legal LLP</div>
      <div>Fennick Court, Wallingford, Oxfordshire OX10 4TJ, United Kingdom</div>
      <div>+44 (0)1632 960457 · post@drvlegal-example.com · www.drvlegal-example.com</div>
    </address>

    <footer class="footer-registration">
      <div>14 Larkspur Row, Brindlecote, Wallingford, Oxfordshire OX10 4TW, United Kingdom</div>
      <div>CRN OC741593 · VAT GB 417386025</div>
    </footer>

    <div class="corner-decoration" role="img" aria-label="Decorative corner graphic of soft green and blue rounded shapes"></div>
  </main>
</body>
</html>
```